Book Cover and Back Cover for Assemble Yourself™ Career Development Manual
Daniel R. Holbrook | Holbrook Advisory, LLC | danielrholbrook.example
Book Cover and Back Cover for Assemble Yourself™ Career Development Manual - Books
Creative Brief
BOOK COVER - blue (RGB 0.0.69) is background/foundational color - the title, "Assemble Yourself™", is orange (RGB 255.54.0), is centered - the subtitle, "A blueprint for utilizing the TRAV assessment to unlock your potential, develop your career, and advance your personal brand." is white, is centered - my name, "Daniel R. Holbrook", is at the bottom, is centered - graphic...I'd like to add a graphic at the bottom of the cover, please review my website, danielrholbrook.example, for ideas. I want it to marry the ideas of business strategy concepts, unlocking human potential, and career growth. BACK COVER - blue (RGB 0.0.69) is background/foundational color - at top center, in orange (RGB 255.54.0), "Inside this manual is the process that will unlock your potential", in a thinly outlined box - in the center is the text "Daniel R. Holbrook is a Licensed Conduct Pattern Examiner (LCPE), a Principal Expert in Staff Affairs (PESA) and a Kestrel Institute of World Commerce MBA graduate. He is owner of Holbrook Advisory, LLC, a coaching practice specializing in unlocking human potential and career advancement, is author of a book entitled Dreading Ordinariness, and is Assistant Director of the L. T. Brandt College of Commerce' Graduate Career Center where he provides career coaching to professional programs MBA students. Daniel is also Vice Chairman of the Phoenix Enterprise and Labor Growth council. Prior to his current roles, he spent more than a decade in recruitment, training and development, and operations management with organizations such as the Bright Harbor Inns and Retreats, VacaLink Worldwide, Meridel Care, and Silver Mesa College." - my picture, from http://danielrholbrook.example/about-2/, is incorporated into the above biography text - standard empty white box for ISBN barcode, at the bottom right - the "Holbrook Advisory" business logo, at bottom left
Books
Working professionals who are: - trying to discover their life's purpose - wanting a promotion at their current job - trying to transition to a different employer - looking for a step-by-step process
JPEG and PDF in 300dpi commercial printing use for 8x11 book cover with bleed

```html
<!DOCTYPE html>
<html lang="en">
<head>
<meta charset="utf-8">
<title>Assemble Yourself™ – Book Cover Spread</title>
<link href="https://fonts.googleapis.com/css2?family=Arimo:ital,wght@0,400;0,700;1,400;1,700&display=swap" rel="stylesheet">
<style>
  :root {
    --navy: #000045;
    --orange: #ff3600;
    --white: #ffffff;
    --page: #f2f2f2;
    --rule: #3a3a72;
  }
  * { box-sizing: border-box; margin: 0; padding: 0; }
  html, body { width: 1200px; height: 847px; overflow: hidden; background: var(--page); }
  body { font-family: "Arimo", Arial, sans-serif; position: relative; }

  .spread {
    position: absolute; left: 54px; top: 146px;
    width: 1092px; height: 555px;
    display: flex; background: var(--navy);
    box-shadow: 0 2px 10px rgba(0,0,0,.25);
  }

  /* Back cover */
  .back { position: relative; width: 547px; height: 100%; }
  .back-tagline {
    position: absolute; left: 36px; top: 34px; width: 410px; height: 52px;
    border: 1px solid var(--orange);
    color: var(--orange); font-weight: 700; font-size: 15px; line-height: 20px;
    display: flex; align-items: center; justify-content: center; text-align: center;
    padding: 0 14px;
  }
  .author-photo {
    position: absolute; left: 17px; top: 161px; width: 77px; height: 84px;
    background: linear-gradient(160deg, #c9cdd6 0%, #8e96a8 55%, #3b4660 100%);
  }
  .bio {
    position: absolute; left: 17px; top: 160px; width: 512px;
    color: var(--white); font-size: 9.4px; line-height: 15px;
  }
  .bio::before {
    content: ""; float: left; width: 84px; height: 88px;
  }
  .bio strong { color: var(--orange); }
  .isbn-box {
    position: absolute; left: 17px; top: 446px; width: 120px; height: 92px;
    background: var(--white);
  }
  .publisher-mark {
    position: absolute; left: 240px; top: 452px; width: 130px;
    display: flex; flex-direction: column; align-items: center; gap: 6px;
    color: var(--white); font-size: 11px; font-weight: 700; letter-spacing: .5px;
  }
  .publisher-mark .dot { width: 22px; height: 22px; border-radius: 50%; background: var(--white); }

  /* Spine */
  .spine {
    position: relative; width: 60px; height: 100%;
    border-left: 1px solid var(--rule); border-right: 1px solid var(--rule);
  }
  .spine-title, .spine-author {
    position: absolute; left: 50%; white-space: nowrap;
    writing-mode: vertical-rl; transform: translateX(-50%);
  }
  .spine-title { top: 44px; color: var(--orange); font-weight: 700; font-size: 24px; }
  .spine-author { bottom: 34px; color: var(--white); font-weight: 700; font-size: 12px; }

  /* Front cover */
  .front { position: relative; width: 485px; height: 100%; text-align: center; }
  .front-title {
    position: absolute; left: 0; right: 0; top: 30px;
    color: var(--orange); font-weight: 700; font-size: 40px; letter-spacing: -.5px;
  }
  .front-title sup { font-size: 16px; vertical-align: 20px; }
  .front-subtitle {
    position: absolute; left: 36px; right: 36px; top: 104px;
    color: var(--white); font-style: italic; font-weight: 700; font-size: 14.5px; line-height: 18px;
  }
  .cover-image {
    position: absolute; left: 24px; top: 178px; width: 437px; height: 300px;
    background: linear-gradient(180deg, #f4f4f4 0%, #dcdcdc 60%, #b9b9b9 100%);
  }
  .front-author {
    position: absolute; left: 0; right: 0; top: 502px;
    color: var(--white); font-weight: 700; font-size: 18px;
  }
</style>
</head>
<body>
  <main class="spread">
    <section class="back">
      <div class="back-tagline">Inside this manual is the process that will unlock your potential</div>
      <div class="author-photo" role="img" aria-label="Portrait photo of author Daniel R. Holbrook"></div>
      <p class="bio"><strong>DANIEL R. HOLBROOK</strong> is a Licensed Conduct Pattern Examiner (LCPE), a Principal Expert in Staff Affairs (PESA) and a Kestrel Institute of World Commerce MBA graduate. He is owner of Holbrook Advisory, LLC, a coaching practice specializing in unlocking human potential and career advancement, is author of a book entitled Dreading Ordinariness, and is Assistant Director of the L. T. Brandt College of Commerce' Graduate Career Center where he provides career coaching to professional programs MBA students. Daniel is also Vice Chairman of the Phoenix Enterprise and Labor Growth council. Prior to his current roles, he spent more than a decade in recruitment, training and development, and operations management with organizations such as the Bright Harbor Inns and Retreats, VacaLink Worldwide, Meridel Care, and Silver Mesa College.</p>
      <div class="isbn-box"></div>
      <div class="publisher-mark"><span class="dot"></span><span>HOLBROOK ADVISORY</span></div>
    </section>

    <section class="spine">
      <span class="spine-title">Assemble Yourself™</span>
      <span class="spine-author">Daniel R. Holbrook</span>
    </section>

    <section class="front">
      <h1 class="front-title">Assemble Yourself<sup>™</sup></h1>
      <p class="front-subtitle">A blueprint for utilizing the TRAV assessment to unlock your potential, develop your career, and advance your personal brand</p>
      <div class="cover-image" role="img" aria-label="Photo of a young professional in front of a whiteboard sketched with business strategy and career growth concepts"></div>
      <p class="front-author">Daniel R. Holbrook</p>
    </section>
  </main>
</body>
</html>
```